Business Card for Managing Partner Investment Fund

To create a business card template for an investment fund manager. Business card should be more professional in nature, not too colorful, more upscale, and created using the attached logos and fund name files. I would prefer a black or gray color scheme, but am open to the use of color as well. I would prefer a double sided business card, but open to single sided business card designs as well. The business card should include: name, title, and contact information, as well as logo and company name. I would prefer a more stream-lined, simple business card design.
Updates
Address: 4136 NE 19th Ter. Ocala, FL 34470
Email: travis48@quillnet-mail.com
Phone: 561-374-9186
Title: managing partner
Name: Travis Whitlow
Fund Name: Emberfall Capital
Logos can be found in files attached to the brief
Target Market(s)
potential investors, other fund managers
Industry/Entity Type
Finance
Contact Information for Business Card
Name on card: Travis Whitlow
Title: Managing Partner
Font styles to use
Colors
Designer to choose colors to be used in the design.
Requirements
Must have
- Phone number
- email address
- physical address
- title
- name
- logo
- Fund name
Nice to have
- simple layout
Should not have
- too many colors, busy fonts,

```html
<!DOCTYPE html>
<html lang="en">
<head>
<meta charset="utf-8">
<title>Emberfall Capital – Business Card</title>
<link href="https://fonts.googleapis.com/css2?family=Cinzel:wght@400&family=Nunito+Sans:wght@300;400&display=swap" rel="stylesheet">
<style>
  :root {
    --page-bg: #2b2b2b;
    --card-black: #050505;
    --card-white: #ffffff;
    --silver-light: #d9d9d9;
    --silver-mid: #a6a6a6;
    --silver-dark: #6e6e6e;
    --ink-gray: #5c5c5c;
    --ink-dark: #333333;
    --rule: #9a9a9a;
  }
  * { margin: 0; padding: 0; box-sizing: border-box; }
  html, body { width: 1200px; height: 900px; overflow: hidden; }
  body {
    background: var(--page-bg);
    position: relative;
    font-family: "Nunito Sans", sans-serif;
  }
  .card {
    position: absolute;
    width: 630px;
    height: 360px;
    box-shadow: 0 14px 30px rgba(0,0,0,0.45);
    overflow: hidden;
  }
  /* Front side */
  .card-front {
    left: 90px;
    top: 70px;
    background: var(--card-black);
  }
  .card-front .fund-name {
    position: absolute;
    left: 150px;
    top: 150px;
    width: 260px;
    text-align: center;
    font-family: "Cinzel", serif;
    font-weight: 400;
    color: var(--silver-light);
    font-size: 34px;
    line-height: 1.05;
    letter-spacing: 1px;
  }
  .card-front .fund-name small {
    display: block;
    font-size: 20px;
    letter-spacing: 6px;
    margin-top: 6px;
  }
  .card-front .decor-panel {
    position: absolute;
    right: 0;
    top: 0;
    width: 190px;
    height: 100%;
    background: linear-gradient(160deg, var(--silver-dark), var(--silver-light) 55%, var(--silver-mid));
  }
  /* Back side */
  .card-back {
    left: 480px;
    top: 470px;
    background: var(--card-white);
  }
  .card-back .fund-name {
    position: absolute;
    left: 34px;
    top: 160px;
    width: 250px;
    text-align: center;
    font-family: "Cinzel", serif;
    font-weight: 400;
    color: var(--ink-gray);
    font-size: 30px;
    line-height: 1.05;
  }
  .card-back .fund-name small {
    display: block;
    font-size: 18px;
    letter-spacing: 6px;
    margin-top: 6px;
  }
  .card-back .divider {
    position: absolute;
    left: 310px;
    top: 100px;
    width: 1px;
    height: 130px;
    background: var(--rule);
  }
  .card-back .contact {
    position: absolute;
    left: 328px;
    top: 102px;
    color: var(--ink-gray);
  }
  .contact .person-name {
    font-family: "Cinzel", serif;
    font-size: 19px;
    letter-spacing: 0.5px;
    line-height: 1;
  }
  .contact .person-title {
    font-size: 14px;
    color: var(--ink-dark);
    margin-bottom: 14px;
  }
  .contact .line {
    display: flex;
    align-items: center;
    gap: 9px;
    font-size: 14px;
    font-weight: 300;
    line-height: 1.55;
  }
  .contact .line svg { width: 11px; height: 11px; fill: var(--ink-dark); flex: none; }
</style>
</head>
<body>

<section class="card card-front" aria-label="Card front">
  <div class="fund-name">EMBERFALL<small>CAPITAL</small></div>
  <div class="decor-panel" role="img" aria-label="Silver decorative artwork area"></div>
</section>

<section class="card card-back" aria-label="Card back">
  <div class="fund-name">EMBERFALL<small>CAPITAL</small></div>
  <div class="divider"></div>
  <div class="contact">
    <div class="person-name">TRAVIS WHITLOW</div>
    <div class="person-title">Managing Partner</div>
    <div class="line">
      <svg viewBox="0 0 24 24" aria-hidden="true"><path d="M6.6 10.8c1.4 2.8 3.8 5.1 6.6 6.6l2.2-2.2c.3-.3.7-.4 1-.2 1.1.4 2.3.6 3.6.6.6 0 1 .4 1 1V20c0 .6-.4 1-1 1C10.6 21 3 13.4 3 4c0-.6.4-1 1-1h3.5c.6 0 1 .4 1 1 0 1.3.2 2.5.6 3.6.1.3 0 .7-.2 1z"/></svg>
      <span>561-374-9186</span>
    </div>
    <div class="line">
      <svg viewBox="0 0 24 24" aria-hidden="true"><path d="M2 5h20v14H2z M2 5l10 8 10-8" fill="none" stroke="#333" stroke-width="0"/><path d="M2 5h20L12 12z M2 7l10 7 10-7v12H2z"/></svg>
      <span>travis48@quillnet-mail.com</span>
    </div>
    <div class="line">
      <svg viewBox="0 0 24 24" aria-hidden="true"><path d="M12 3l10 9h-3v9h-5v-6h-4v6H5v-9H2z"/></svg>
      <span>4136 NE 19th Ter. Ocala, FL 34470</span>
    </div>
  </div>
</section>

</body>
</html>
```